MEDICAL GRANT GRAPHIC FOR SCIENTIFIC STUDY

FOR A GRANT, WE NEED A GRAPHIC THAT REFLECTS THE ISSUES IN OUR GRANT.
COLORS: BLUE/GREEENS
I AM UPLOADING TWO GRAPHICS.
THE SECOND ONE IS A BALANCE WHICH NEEDS TO BE INCLUDED IN THE FIRST GRAPHIC. THE BALANCE IS EQUAL IN THE GRAPHIC I HAVE DONE. HOWEVER, FOR THE FINAL PRODUCT, THE BALANCE NEEDS TO BE LOWER ON THE END WITH 'PATIENT WORKLOAD'

Target Market(s)

GRANT FUNDERS

Font styles to use
Sans Serif

Colors
0094D4
00A9DD
6FCCEA
C7EBF8
E9F6FB

```html
<!DOCTYPE html>
<html lang="en">
<head>
<meta charset="utf-8">
<title>Consumer Advisory Group Engagement</title>
<link href="https://fonts.googleapis.com/css2?family=Inter:wght@400;600;700&display=swap" rel="stylesheet">
<style>
  :root {
    --page-bg: #34aed3;
    --card-bg: #ffffff;
    --blue-deep: #2fa9d0;
    --blue-mid: #4dbbe2;
    --blue-light: #8fd6fb;
    --accent: #36aad6;
    --ink: #111111;
  }
  html, body {
    margin: 0;
    padding: 0;
    width: 1200px;
    height: 1122px;
    overflow: hidden;
    background: var(--page-bg);
    font-family: "Inter", "Helvetica Neue", Arial, sans-serif;
  }
  .canvas { display: block; width: 1200px; height: 1122px; }
  .theme-title { font-weight: 700; font-size: 16px; fill: #fff; letter-spacing: -0.5px; }
  .theme-label { font-weight: 400; font-size: 16px; fill: var(--ink); letter-spacing: -0.4px; }
  .hub-title { font-weight: 700; font-size: 28px; fill: #fff; letter-spacing: -0.8px; }
  .balance-label { font-weight: 700; font-size: 24px; fill: var(--accent); letter-spacing: -0.6px; }
  .flow-solid { stroke: var(--ink); stroke-width: 0.8; fill: none; }
  .flow-dashed { stroke: var(--ink); stroke-width: 0.8; stroke-dasharray: 5 5; fill: none; }
  .frame-line { stroke: var(--accent); stroke-width: 1.2; fill: none; }
  .balance-beam { stroke: var(--accent); stroke-width: 1.6; fill: none; }
  .balance-pivot { fill: var(--accent); }
</style>
</head>
<body>
<svg class="canvas" viewBox="0 0 1200 1122" xmlns="http://www.w3.org/2000/svg">
  <defs>
    <linearGradient id="bar-top" x1="0" x2="1" y1="0" y2="0">
      <stop offset="0" stop-color="var(--blue-deep)"/>
      <stop offset="1" stop-color="var(--blue-light)"/>
    </linearGradient>
    <linearGradient id="bar-bottom" x1="0" x2="1" y1="0" y2="0">
      <stop offset="0" stop-color="var(--blue-light)"/>
      <stop offset="1" stop-color="var(--blue-deep)"/>
    </linearGradient>
    <linearGradient id="orb-fill" x1="0" x2="1" y1="0.2" y2="0">
      <stop offset="0" stop-color="#2ea8d2"/>
      <stop offset="1" stop-color="#92d8fd"/>
    </linearGradient>
    <linearGradient id="orb-rim" x1="0" x2="1" y1="0" y2="1">
      <stop offset="0" stop-color="#8ed5fa"/>
      <stop offset="1" stop-color="#2fa6cf"/>
    </linearGradient>
    <marker id="head" viewBox="0 0 10 10" refX="9" refY="5" markerWidth="7" markerHeight="7" orient="auto-start-reverse">
      <path d="M0 0 L10 5 L0 10 Z" fill="#111"/>
    </marker>
    <marker id="head-accent" viewBox="0 0 10 10" refX="9" refY="5" markerWidth="10" markerHeight="10" orient="auto-start-reverse" markerUnits="userSpaceOnUse">
      <path d="M0 0 L10 5 L0 10 Z" fill="#36aad6"/>
    </marker>
  </defs>

  <!-- card -->
  <g class="card">
    <rect x="24" y="240" width="1152" height="643" fill="var(--card-bg)"/>
    <rect x="24" y="240" width="1152" height="10" fill="url(#bar-top)"/>
    <rect x="24" y="873" width="1152" height="10" fill="url(#bar-bottom)"/>
  </g>

  <!-- outer frame feeding the balance -->
  <g class="frame">
    <polyline class="frame-line" points="109,760 109,295 1093,295 1093,760"/>
    <path d="M103 757 L115 757 L109 767 Z" fill="var(--accent)"/>
    <path d="M1087 757 L1099 757 L1093 767 Z" fill="var(--accent)"/>
  </g>

  <!-- flows between themes -->
  <g class="flows">
    <line class="flow-dashed" x1="398" y1="371" x2="803" y2="371" marker-end="url(#head)"/>
    <polyline class="flow-dashed" points="267,714 267,740 1057,740 1057,369 978,369" marker-end="url(#head)"/>
    <line class="flow-dashed" x1="268" y1="476" x2="268" y2="566" marker-start="url(#head)" marker-end="url(#head)"/>
    <line class="flow-dashed" x1="889" y1="474" x2="889" y2="566" marker-end="url(#head)"/>
    <line class="flow-solid" x1="500" y1="486" x2="410" y2="447" marker-end="url(#head)"/>
    <line class="flow-solid" x1="701" y1="486" x2="793" y2="447" marker-end="url(#head)"/>
    <line class="flow-solid" x1="478" y1="581" x2="410" y2="610" marker-end="url(#head)"/>
    <line class="flow-solid" x1="724" y1="581" x2="793" y2="610" marker-end="url(#head)"/>
  </g>

  <!-- hub -->
  <g class="hub">
    <circle cx="601" cy="560" r="125" fill="url(#orb-rim)"/>
    <circle cx="601" cy="560" r="116" fill="url(#orb-fill)"/>
    <text class="hub-title" text-anchor="middle" x="602" y="519">CONSUMER</text>
    <text class="hub-title" text-anchor="middle" x="602" y="551">ADVISORY</text>
    <text class="hub-title" text-anchor="middle" x="602" y="582">GROUP</text>
    <text class="hub-title" text-anchor="middle" x="602" y="614">ENGAGEMENT</text>
  </g>

  <!-- themes -->
  <g class="theme">
    <circle cx="268" cy="369" r="44" fill="url(#orb-rim)"/>
    <circle cx="268" cy="369" r="40" fill="url(#orb-fill)"/>
    <text class="theme-title" text-anchor="middle" x="268" y="375">THEME 1</text>
    <text class="theme-label" text-anchor="middle" x="268" y="432">Identifying Complex Patients</text>
    <text class="theme-label" text-anchor="middle" x="268" y="451">with Rheumatic Diseases</text>
  </g>
  <g class="theme">
    <circle cx="268" cy="620" r="44" fill="url(#orb-rim)"/>
    <circle cx="268" cy="620" r="40" fill="url(#orb-fill)"/>
    <text class="theme-title" text-anchor="middle" x="268" y="626">THEME 2</text>
    <text class="theme-label" text-anchor="middle" x="268" y="680">Consumer Voice</text>
  </g>
  <g class="theme">
    <circle cx="889" cy="369" r="44" fill="url(#orb-rim)"/>
    <circle cx="889" cy="369" r="40" fill="url(#orb-fill)"/>
    <text class="theme-title" text-anchor="middle" x="889" y="375">THEME 3</text>
    <text class="theme-label" text-anchor="middle" x="889" y="432">Interventions to</text>
    <text class="theme-label" text-anchor="middle" x="889" y="451">Optimise Management</text>
  </g>
  <g class="theme">
    <circle cx="889" cy="620" r="44" fill="url(#orb-rim)"/>
    <circle cx="889" cy="620" r="40" fill="url(#orb-fill)"/>
    <text class="theme-title" text-anchor="middle" x="889" y="626">THEME 4</text>
    <text class="theme-label" text-anchor="middle" x="889" y="680">Improve Outcomes and</text>
    <text class="theme-label" text-anchor="middle" x="889" y="700">Quality of Life</text>
  </g>

  <!-- balance: tipped down toward workload -->
  <g class="balance">
    <line class="balance-beam" x1="268" y1="780" x2="935" y2="808" marker-start="url(#head-accent)" marker-end="url(#head-accent)"/>
    <path class="balance-pivot" d="M601 795 L591 812 L611 812 Z"/>
    <text class="balance-label" text-anchor="middle" x="174" y="786">PATIENT</text>
    <text class="balance-label" text-anchor="middle" x="174" y="814">CAPACITY</text>
    <text class="balance-label" text-anchor="middle" x="1026" y="806">PATIENT</text>
    <text class="balance-label" text-anchor="middle" x="1026" y="834">WORKLOAD</text>
  </g>
</svg>
</body>
</html>
```